Stationery Refresh For Local Mortgage Broker

We want to modernise and standardise our stationery, including: letterhead, presentation folder, email signature and business card.

The new stationery should be a more modern and professional take on our existing colour scheme and brand. (We do not want a complete overhaul.) A folder of approved stock photos can be found here: https://filebox.example-share.net/f/7kQzR2mTn4vWx9Lp3Yb8-HsdJe5Uc1Ga/view

Our current website is: www.brindlecovefin.com.au but we will be updating this to be consistent with our new stationery.

We are open to *very slight* tweaks to our logo if you feel it needs modernising, but overall we would like to maintain consistent colour scheme.

> Letterhead

148 Calloway Parade,
Geelong, VIC, 3220
ABN: 31 805 249 067
Australian Credit License: 718293

(03) 5391 6084
www.brindlecovefin.com.au

> Presentation Folder

148 Calloway Parade,
Geelong, VIC, 3220
(03) 5391 6084
www.brindlecovefin.com.au

ABN: 31 805 249 067

> Email Signature

Liam Tresidder
Director
M. 0412 857 294
P. (03) 5391 6084
www.brindlecovefin.com.au
148 Calloway Parade,
Geelong, VIC, 3220

ABN: 31 805 249 067

(you can also include a photo if you like: https://brindlecovefin.com.au/wp-content/uploads/2020/12/Liam-Tresidder.png.webp)

> Business Card

Liam Tresidder
Director
M. 0412 857 294
P. (03) 5391 6084
www.brindlecovefin.com.au
148 Calloway Parade,
Geelong, VIC, 3220

ABN: 31 805 249 067

Additional information...

If it's useful/relevant, the services we offer are: Home Loans, Investment Loans, Refinance, Debt Consolidation, Commercial Finance, Vehicle Loans
(You may choose to use this in any of the designs)

Target Market(s)

Home Buyers and Investors

Industry/Entity Type

Mortgage broking/property/real estate

Requirements
Must have
• At least somewhat consistent with our current site (yet meaningfully modernized)
Should not have
• dramatically different logo or colourscheme overhauls

```html
<!DOCTYPE html>
<html lang="en">
<head>
<meta charset="utf-8">
<title>Brindle Cove Financial Services — Stationery Suite</title>
<link href="https://fonts.googleapis.com/css2?family=Montserrat:wght@400;500&family=Roboto:wght@400;500;700&display=swap" rel="stylesheet">
<style>
  :root{
    --bg:#ececec;
    --paper:#f7f7f7;
    --paper-shade:#efefef;
    --red:#b8282b;
    --red-dark:#8c1d1f;
    --red-bright:#d0373a;
    --ink:#2e2e2e;
    --ink-soft:#666;
    --grey-band:#4a4a4c;
    --white:#ffffff;
  }
  *{box-sizing:border-box;margin:0;padding:0}
  html,body{width:1200px;height:795px;overflow:hidden;background:var(--bg)}
  body{position:relative;font-family:"Roboto",Arial,sans-serif;color:var(--ink)}
  .sheet{position:absolute;background:var(--paper);box-shadow:0 2px 6px rgba(0,0,0,.12);overflow:hidden}

  .brand{font-family:"Montserrat",Arial,sans-serif;color:var(--red);line-height:1;text-align:center;display:inline-block}
  .brand__name{font-weight:400;letter-spacing:.22em;white-space:nowrap}
  .brand__tag{font-weight:400;letter-spacing:.32em;color:var(--ink-soft);white-space:nowrap;margin-top:3px}

  /* Letterhead */
  .letterhead{left:293px;top:99px;width:292px;height:415px}
  .letterhead .brand{position:absolute;left:18px;top:38px}
  .letterhead .brand__name{font-size:11px}
  .letterhead .brand__tag{font-size:4.6px}
  .letterhead__contact{position:absolute;right:18px;top:31px;text-align:right;font-size:5.2px;line-height:7.6px}
  .letterhead__contact .dot{display:inline-block;width:4px;height:4px;border-radius:50%;background:var(--red);margin-left:3px;vertical-align:middle}
  .letterhead__contact .label{color:var(--red)}
  .letter{position:absolute;left:18px;top:156px;width:256px;font-size:4.6px;line-height:6.7px;color:#555}
  .letter p{margin-bottom:6px;text-align:justify}
  .letter .recipient{font-weight:700;color:#444}
  .letterhead__foot{position:absolute;left:0;bottom:0;width:100%;height:18px}

  /* Email signature */
  .signature{left:140px;top:334px;width:326px;height:102px;background:#f4f4f4}
  .signature__photo{position:absolute;left:14px;top:8px;width:82px;height:84px;border-radius:48% 52% 45% 55%/55% 45% 55% 45%;background:linear-gradient(160deg,#d9dde2,#aeb4bb 55%,#3a3d44)}
  .signature .brand{position:absolute;left:125px;top:14px}
  .signature .brand__name{font-size:13px}
  .signature .brand__tag{font-size:5.4px}
  .signature__name{position:absolute;left:125px;top:47px;font-size:8.6px;font-weight:500;color:var(--red-dark)}
  .signature__role{position:absolute;left:125px;top:57px;font-size:5.6px;color:var(--ink-soft)}
  .signature__details{position:absolute;left:125px;top:67px;display:grid;grid-template-columns:60px auto;column-gap:4px;row-gap:3px;font-size:5.6px}
  .signature__details span{display:flex;align-items:center;gap:5px;white-space:nowrap}
  .signature__details svg{width:6px;height:6px;flex:none}
  .signature__bar{position:absolute;left:0;bottom:0;width:100%;height:12px}
  .signature__bar-text{position:absolute;left:126px;bottom:2px;font-size:4.6px;color:var(--white);white-space:nowrap}

  /* Folder */
  .folder{left:636px;top:78px;width:346px;height:438px;background:#f1f1f1}
  .folder svg.folder__art{position:absolute;left:0;top:0}
  .folder .brand{position:absolute;left:20px;top:48px}
  .folder .brand__name{font-size:9.6px}
  .folder .brand__tag{font-size:4.2px}
  .folder__title{position:absolute;left:19px;top:342px;color:var(--white);font-family:"Montserrat",Arial,sans-serif;line-height:1}
  .folder__title small{display:block;font-size:9px;letter-spacing:.04em;margin-bottom:3px}
  .folder__title strong{font-weight:400;font-size:15px;letter-spacing:.05em}
  .folder__legal{position:absolute;left:19px;top:402px;font-size:6.2px;line-height:9.6px;color:var(--white)}
  .folder__contact{position:absolute;right:25px;top:392px;font-size:6.2px;line-height:9.6px;color:var(--white);text-align:right}
  .folder__contact .dot{display:inline-block;width:4px;height:4px;border-radius:50%;background:var(--white);margin-left:5px;vertical-align:middle}

  /* Business cards */
  .card{width:133px;height:75px}
  .card--front{left:186px;top:550px;background:linear-gradient(135deg,var(--red),var(--red-dark))}
  .card--front .brand{position:absolute;left:0;width:100%;top:14px;color:var(--white)}
  .card--front .brand__name{font-size:8.4px}
  .card--front .brand__tag{font-size:3.8px;color:#f0c9ca}
  .card__pill{position:absolute;left:46px;top:41px;width:41px;height:6px;border-radius:3px;background:var(--red-bright);color:var(--white);font-size:3.4px;text-align:center;line-height:6px;letter-spacing:.05em}
  .card__services{position:absolute;left:0;top:46px;width:100%;height:17px;background:var(--grey-band);color:#e8e8e8;font-size:3.4px;line-height:5px;text-align:center;padding-top:4px}
  .card__legal{position:absolute;left:0;bottom:3px;width:100%;text-align:center;font-size:3.2px;color:#f5dcdc}
  .card--back{left:186px;top:646px;background:var(--paper)}
  .card--back .brand{position:absolute;left:7px;top:9px}
  .card--back .brand__name{font-size:8.4px}
  .card--back .brand__tag{font-size:3.8px}
  .card__name{position:absolute;left:7px;top:30px;font-size:5px;font-weight:700;color:var(--red-dark)}
  .card__role{position:absolute;left:7px;top:36px;font-size:3.4px;color:var(--ink-soft)}
  .card__licence{position:absolute;left:7px;top:46px;font-size:3.2px;line-height:4.4px;color:var(--red-dark);font-weight:700}
  .card__contact{position:absolute;right:7px;top:50px;font-size:3.4px;line-height:4.6px;text-align:right;color:var(--ink);z-index:2}
  .card--back svg{position:absolute;left:0;top:0}

  /* Envelopes */
  .envelope{width:329px;height:157px;background:#f3f3f1}
  .envelope--front{left:353px;top:562px}
  .envelope--front .brand{position:absolute;left:24px;top:23px}
  .envelope--front .brand__name{font-size:11px}
  .envelope--front .brand__tag{font-size:4.6px}
  .envelope__address{position:absolute;left:24px;top:129px;font-size:6.4px;color:var(--ink-soft)}
  .envelope--back{left:714px;top:562px;width:327px;background:#f6f6f6}
  .envelope--back svg{position:absolute;left:0;top:0}
  .envelope__url{position:absolute;left:110px;top:26px;font-family:"Montserrat",Arial,sans-serif;font-size:5.2px;letter-spacing:.36em;color:#f3d4d4;white-space:nowrap}
</style>
</head>
<body>

  <!-- Letterhead -->
  <section class="sheet letterhead" aria-label="Letterhead">
    <div class="brand">
      <div class="brand__name">BRINDLE COVE</div>
      <div class="brand__tag">FINANCIAL SERVICES</div>
    </div>
    <div class="letterhead__contact">
      <div>(03) 5391 6084<span class="dot"></span></div>
      <div>www.brindlecovefin.com.au<span class="dot"></span></div>
      <div>148 Calloway Parade, Geelong, VIC, 3220</div>
      <div><span class="label">ABN:</span> 31 805 249 067 &nbsp;|&nbsp; <span class="label">ACL:</span> 718293</div>
    </div>
    <div class="letter">
      <p>30/20/2016</p>
      <p style="margin-top:10px"><span class="recipient">Mr. XYZ Smith</span><br>123, Street No. 123,<br>City Name<br>Pincode-123456</p>
      <p style="margin-top:10px">Dear Sir,</p>
      <p style="margin-top:10px">Thank you for the opportunity to assist with your home loan. This letter sets out the next steps in your application, the documents we still need from you, and the timeline we expect for approval. Please read it carefully and contact our office if anything is unclear.</p>
      <p>Our broker will compare offers from a wide panel of lenders and explain the fees, rates and features of each option. Once you choose a loan, we will prepare the paperwork and keep you updated at every stage until settlement is complete.</p>
      <p>We look forward to working with you and helping you reach your property goals this year.</p>
    </div>
    <svg class="letterhead__foot" viewBox="0 0 292 18" preserveAspectRatio="none">
      <path d="M0 6 C90 14 200 12 292 8 V18 H0 Z" fill="var(--red)"/>
      <path d="M0 3 C90 11 200 9 292 5" stroke="#d9d9d9" stroke-width="1.2" fill="none"/>
    </svg>
  </section>

  <!-- Email signature -->
  <section class="sheet signature" aria-label="Email signature">
    <div class="signature__photo" role="img" aria-label="Portrait photo of Liam Tresidder"></div>
    <div class="brand">
      <div class="brand__name">BRINDLE COVE</div>
      <div class="brand__tag">FINANCIAL SERVICES</div>
    </div>
    <div class="signature__name">Liam Tresidder</div>
    <div class="signature__role">Director</div>
    <div class="signature__details">
      <span><svg viewBox="0 0 10 10"><circle cx="5" cy="5" r="4" fill="none" stroke="var(--red)" stroke-width="1.4"/><path d="M3 7 7 3" stroke="var(--red)" stroke-width="1.4"/></svg>0412 857 294</span>
      <span><svg viewBox="0 0 10 10"><circle cx="5" cy="5" r="4" fill="var(--red)"/></svg>www.brindlecovefin.com.au</span>
      <span><svg viewBox="0 0 10 10"><path d="M1 4 Q5 0 9 4 L7 5 6 4 H4 L3 5 Z M2.5 5.5 H7.5 V9 H2.5 Z" fill="var(--red)"/></svg>(03) 5391 6084</span>
      <span><svg viewBox="0 0 10 10"><path d="M5 0.5 C2.5 0.5 1.2 2.3 1.2 4.2 C1.2 6.8 5 9.5 5 9.5 S8.8 6.8 8.8 4.2 C8.8 2.3 7.5 0.5 5 0.5 Z" fill="var(--red)"/><circle cx="5" cy="4.2" r="1.4" fill="#f4f4f4"/></svg>148 Calloway Parade, Geelong, VIC, 3220</span>
    </div>
    <svg class="signature__bar" viewBox="0 0 326 12" preserveAspectRatio="none">
      <rect x="0" y="7" width="140" height="3" fill="var(--red)"/>
      <path d="M112 0 H326 V12 H106 Z" fill="var(--red-dark)"/>
    </svg>
    <div class="signature__bar-text">Australian Credit License: 718293 &nbsp;|&nbsp; ABN: 31 805 249 067</div>
  </section>

  <!-- Presentation folder -->
  <section class="sheet folder" aria-label="Presentation folder">
    <svg class="folder__art" width="346" height="438" viewBox="0 0 346 438">
      <defs>
        <linearGradient id="scene" x1="0" y1="0" x2="0" y2="1">
          <stop offset="0" stop-color="#d9dfe3"/>
          <stop offset=".5" stop-color="#b9cbd3"/>
          <stop offset=".75" stop-color="#6f98a6"/>
          <stop offset="1" stop-color="#3f6a58"/>
        </linearGradient>
        <linearGradient id="folderRed" x1="0" y1="0" x2="1" y2="1">
          <stop offset="0" stop-color="var(--red)"/>
          <stop offset="1" stop-color="var(--red-dark)"/>
        </linearGradient>
      </defs>
      <rect x="0" y="95" width="346" height="240" fill="url(#scene)" role="img" aria-label="Photo of a waterfront city with a Ferris wheel and pier"/>
      <path d="M0 0 H346 V112 C260 122 110 128 0 96 Z" fill="#f1f1f1"/>
      <path d="M0 88 C90 118 200 120 240 110 C180 128 70 130 0 118 Z" fill="url(#folderRed)"/>
      <path d="M0 286 C90 322 240 316 346 296" stroke="#f4f4f4" stroke-width="9" fill="none"/>
      <path d="M0 296 C90 332 240 326 346 304 V438 H0 Z" fill="url(#folderRed)"/>
      <rect x="4" y="0" width="1" height="438" fill="rgba(0,0,0,.08)"/>
    </svg>
    <div class="brand">
      <div class="brand__name">BRINDLE COVE</div>
      <div class="brand__tag">FINANCIAL SERVICES</div>
    </div>
    <div class="folder__title"><small>Presentation</small><strong>FOLDER</strong></div>
    <div class="folder__legal">ABN: 31 805 249 067<br>Australian Credit License: 718293</div>
    <div class="folder__contact">
      <div>(03) 5391 6084<span class="dot"></span></div>
      <div>www.brindlecovefin.com.au<span class="dot"></span></div>
      <div>148 Calloway Parade, Geelong, VIC, 3220<span class="dot"></span></div>
    </div>
  </section>

  <!-- Business card front -->
  <section class="sheet card card--front" aria-label="Business card front">
    <div class="brand">
      <div class="brand__name">BRINDLE COVE</div>
      <div class="brand__tag">FINANCIAL SERVICES</div>
    </div>
    <div class="card__services">Home Loans | Investment Loans | Debt Consolidation<br>Commercial Finance | Vehicle Loans | Refinance</div>
    <div class="card__pill">OUR SERVICES</div>
    <div class="card__legal">ABN: 31 805 249 067 &nbsp;|&nbsp; Australian Credit License: 718293</div>
  </section>

  <!-- Business card back -->
  <section class="sheet card card--back" aria-label="Business card back">
    <svg width="133" height="75" viewBox="0 0 133 75">
      <path d="M0 62 C40 42 90 58 133 42 V75 H0 Z" fill="#ececec"/>
      <path d="M0 60 C40 38 90 54 133 38" stroke="var(--grey-band)" stroke-width="3" fill="none"/>
      <path d="M0 64 C40 44 90 60 133 44" stroke="var(--red)" stroke-width="2.4" fill="none"/>
      <rect x="0" y="73" width="133" height="2" fill="var(--red)"/>
    </svg>
    <div class="brand">
      <div class="brand__name">BRINDLE COVE</div>
      <div class="brand__tag">FINANCIAL SERVICES</div>
    </div>
    <div class="card__name">Liam Tresidder</div>
    <div class="card__role">Director</div>
    <div class="card__licence">Australian Credit License: 718293<br>ABN: 31 805 249 067</div>
    <div class="card__contact">M. 0412 857 294<br>P. (03) 5391 6084<br>www.brindlecovefin.com.au<br>148 Calloway Parade, Geelong, VIC, 3220</div>
  </section>

  <!-- Envelope front -->
  <section class="sheet envelope envelope--front" aria-label="Envelope front">
    <div class="brand">
      <div class="brand__name">BRINDLE COVE</div>
      <div class="brand__tag">FINANCIAL SERVICES</div>
    </div>
    <div class="envelope__address">148 Calloway Parade, Geelong, VIC, 3220</div>
  </section>

  <!-- Envelope back -->
  <section class="sheet envelope envelope--back" aria-label="Envelope back">
    <svg width="327" height="157" viewBox="0 0 327 157">
      <defs>
        <linearGradient id="flapRed" x1="0" y1="0" x2="1" y2="0">
          <stop offset="0" stop-color="var(--red)"/>
          <stop offset="1" stop-color="var(--red-dark)"/>
        </linearGradient>
      </defs>
      <path d="M0 0 H327 L323 58 Q322 62 318 62 H11 Q7 62 6 58 Z" fill="url(#flapRed)"/>
    </svg>
    <div class="envelope__url">www.brindlecovefin.com.au</div>
  </section>

</body>
</html>
```